Partnership Enterprise Architects looking for Business Flyer (Dutch laguage)

We are a partnership of independent IT Architects working in various roles within our clients (Goverment agencies, Financial institutions and for profit companies). With this flyer we would like to promote ourselves in a inviting but still business like way. We would like to see our logo and name (Maatschap Tolvera) and the graphs and text we used in our example as the basis of the flyer. Anything else is up to your creativity. Colors and 'look and feel' of the graphs may be altered as long as the text (Dutch language remains unchanged). We think a 2 page A4 format flyer would serve best, but are open to suggestions.

Target Market(s)

Clients in the field of Government agencies, Financial institutions and for profit comapnies as well as possible future partners in the ICT Architect field

Industry/Entity Type

Business

Font styles to use
Sans Serif
Other font styles liked:
• Calibri 11 is our standard font

Colors

Designer to choose colors to be used in the design.

Requirements
Must have
• The text (verbatim in the Dutch laguage) as well as the graphs (they may be altered as you see fit as long as the general point and meaning remain the same). Logo preferably upper right corner. 2 A4 double sided flyer in one piece (

```html
<!DOCTYPE html>
<html lang="nl">
<head>
<meta charset="utf-8">
<title>The Tolvera Group e-CF Groepsprofile</title>
<link rel="stylesheet" href="https://fonts.googleapis.com/css2?family=Source+Sans+3:ital,wght@0,400;0,600;0,700;1,400&display=swap">
<style>
  :root {
    --cream: #fff2cc;
    --title: #7030a0;
    --plan-head: #4b0099;
    --plan-row-a: #d5b6fb;
    --plan-row-b: #e4cffc;
    --build-head: #ffd966;
    --build-row-a: #fde9a8;
    --build-row-b: #fef3cf;
    --enable-head: #70ad47;
    --enable-row-a: #c5e0b3;
    --enable-row-b: #e2efd9;
    --manage-head: #5b9bd5;
    --manage-row-a: #a9cdef;
    --manage-row-b: #d1e4f6;
    --dot-avg: #ffff00;
    --dot-high: #92d050;
    --teal: #7fcfc0;
    --pattern: #e6cf3a;
    --footer: #3d4155;
    --ink: #1a1a1a;
  }
  * { margin: 0; padding: 0; box-sizing: border-box; }
  html, body { width: 848px; height: 1200px; overflow: hidden; }
  body {
    position: relative;
    background: var(--cream);
    font-family: "Source Sans 3", sans-serif;
    color: var(--ink);
  }
  .page-title {
    position: absolute; top: 100px; left: 0; width: 848px;
    text-align: center; font-size: 20px; font-weight: 700; color: var(--title);
  }
  .levels-caption {
    position: absolute; left: 487px; top: 151px; width: 303px; height: 24px;
    background: #d9d9d9; border: 1.5px solid #333; border-bottom: none;
    text-align: center; font-style: italic; font-weight: 600; font-size: 16px; line-height: 22px;
  }
  .profile {
    position: absolute; left: 48px; top: 175px;
    border-collapse: collapse; table-layout: fixed; width: 742px;
    font-size: 14px;
  }
  .profile td { height: 24.27px; border: 1px solid #fff; padding: 0 4px; white-space: nowrap; }
  .profile col.code { width: 58px; }
  .profile col.name { width: 381px; }
  .profile col.level { width: 60.6px; }
  .profile .lvl { text-align: center; padding: 0; }
  .head td { font-weight: 600; color: #fff; }
  .head .lvl { font-weight: 400; }
  .plan.head td { background: var(--plan-head); }
  .build.head td { background: var(--build-head); color: #8a8a8a; }
  .enable.head td { background: var(--enable-head); }
  .manage.head td { background: var(--manage-head); }
  .plan .code { background: var(--plan-head); color: #fff; font-weight: 700; }
  .build .code { background: var(--build-row-a); color: #8a8a8a; font-weight: 700; }
  .enable .code { background: var(--enable-head); color: #fff; font-weight: 700; }
  .manage .code { background: var(--manage-head); color: #fff; font-weight: 700; }
  .plan.a td:not(.code) { background: var(--plan-row-a); }
  .plan.b td:not(.code) { background: var(--plan-row-b); }
  .build.a td:not(.code) { background: var(--build-row-a); }
  .build.b td:not(.code) { background: var(--build-row-b); }
  .enable.a td:not(.code) { background: var(--enable-row-a); }
  .enable.b td:not(.code) { background: var(--enable-row-b); }
  .manage.a td:not(.code) { background: var(--manage-row-a); }
  .manage.b td:not(.code) { background: var(--manage-row-b); }
  .dot {
    display: inline-block; width: 18px; height: 18px; border-radius: 50%;
    border: 1px solid #555; vertical-align: middle;
  }
  .dot.avg { background: var(--dot-avg); }
  .dot.high { background: var(--dot-high); }
  .dot + .dot { margin-left: 2px; }
  .legend { position: absolute; left: 80px; top: 638px; font-style: italic; font-size: 16.5px; color: var(--title); }
  .legend li { list-style: none; display: flex; align-items: center; gap: 9px; height: 25px; }
  .legend .dot { width: 20px; height: 20px; }
  .pattern-band { position: absolute; left: 0; top: 752px; width: 848px; height: 274px; background: var(--pattern); }
  .arc { position: absolute; left: 0; top: 700px; }
  .footer-band { position: absolute; left: 0; top: 1026px; width: 848px; height: 174px; background: var(--footer); border-top: 14px solid #5a5e70; }
</style>
</head>
<body>
  <h1 class="page-title">The Tolvera Group e-CF Groepsprofile - CORE Competences</h1>
  <div class="levels-caption">e-CF levels</div>

  <table class="profile">
    <colgroup><col class="code"><col class="name"><col class="level"><col class="level"><col class="level"><col class="level"><col class="level"></colgroup>
    <tr class="plan head"><td>A</td><td>PLAN</td><td class="lvl">e-1</td><td class="lvl">e-2</td><td class="lvl">e-3</td><td class="lvl">e-4</td><td class="lvl">e-5</td></tr>
    <tr class="plan a"><td class="code">A.1</td><td>IS and Business Strategy Alignment</td><td class="lvl"></td><td class="lvl"></td><td class="lvl"><span class="dot avg"></span></td><td class="lvl"></td><td class="lvl"><span class="dot high"></span></td></tr>
    <tr class="plan b"><td class="code">A.5</td><td>Architecture Design</td><td class="lvl"></td><td class="lvl"></td><td class="lvl"><span class="dot avg"></span></td><td class="lvl"></td><td class="lvl"><span class="dot high"></span></td></tr>
    <tr class="plan a"><td class="code">A.7</td><td>Technology Trend Monitoring</td><td class="lvl"></td><td class="lvl"></td><td class="lvl"></td><td class="lvl"></td><td class="lvl"><span class="dot avg"></span><span class="dot high"></span></td></tr>
    <tr class="plan b"><td class="code">A.9</td><td>Innovating</td><td class="lvl"></td><td class="lvl"></td><td class="lvl"></td><td class="lvl"><span class="dot avg"></span><span class="dot high"></span></td><td class="lvl"></td></tr>

    <tr class="build head"><td>B</td><td>BUILD</td><td class="lvl">e-1</td><td class="lvl">e-2</td><td class="lvl">e-3</td><td class="lvl">e-4</td><td class="lvl">e-5</td></tr>
    <tr class="build a"><td class="code">B.2</td><td>Component Integration</td><td class="lvl"></td><td class="lvl"></td><td class="lvl"><span class="dot avg"></span></td><td class="lvl"><span class="dot high"></span></td><td class="lvl"></td></tr>
    <tr class="build b"><td class="code">B.6</td><td>Systems Engineering</td><td class="lvl"></td><td class="lvl"></td><td class="lvl"><span class="dot avg"></span></td><td class="lvl"><span class="dot high"></span></td><td class="lvl"></td></tr>

    <tr class="enable head"><td>D</td><td>ENABLE</td><td class="lvl">e-1</td><td class="lvl">e-2</td><td class="lvl">e-3</td><td class="lvl">e-4</td><td class="lvl">e-5</td></tr>
    <tr class="enable a"><td class="code">D.1</td><td>Information Security Strategy Development</td><td class="lvl"></td><td class="lvl"></td><td class="lvl"></td><td class="lvl"><span class="dot avg"></span></td><td class="lvl"><span class="dot high"></span></td></tr>
    <tr class="enable b"><td class="code">D.2</td><td>ICT Quality Strategy Development</td><td class="lvl"></td><td class="lvl"></td><td class="lvl"><span class="dot avg"></span></td><td class="lvl"></td><td class="lvl"><span class="dot high"></span></td></tr>
    <tr class="enable a"><td class="code">D.10</td><td>Information and Knowledge Management</td><td class="lvl"></td><td class="lvl"></td><td class="lvl"></td><td class="lvl"></td><td class="lvl"><span class="dot avg"></span><span class="dot high"></span></td></tr>
    <tr class="enable b"><td class="code">D.11</td><td>Needs Identification</td><td class="lvl"></td><td class="lvl"></td><td class="lvl"></td><td class="lvl"><span class="dot avg"></span></td><td class="lvl"><span class="dot high"></span></td></tr>

    <tr class="manage head"><td>E</td><td>MANAGE</td><td class="lvl">e-1</td><td class="lvl">e-2</td><td class="lvl">e-3</td><td class="lvl">e-4</td><td class="lvl">e-5</td></tr>
    <tr class="manage a"><td class="code">E.2</td><td>Project and Portfolio Management</td><td class="lvl"></td><td class="lvl"></td><td class="lvl"><span class="dot avg"></span></td><td class="lvl"></td><td class="lvl"><span class="dot high"></span></td></tr>
    <tr class="manage b"><td class="code">E.6</td><td>ICT Quality Management</td><td class="lvl"></td><td class="lvl"></td><td class="lvl"><span class="dot avg"></span></td><td class="lvl"><span class="dot high"></span></td><td class="lvl"></td></tr>
    <tr class="manage a"><td class="code">E.7</td><td>Business Change Management</td><td class="lvl"></td><td class="lvl"></td><td class="lvl"></td><td class="lvl"><span class="dot avg"></span></td><td class="lvl"><span class="dot high"></span></td></tr>
    <tr class="manage b"><td class="code">E.9</td><td>IS Governance</td><td class="lvl"></td><td class="lvl"></td><td class="lvl"><span class="dot avg"></span></td><td class="lvl"></td><td class="lvl"><span class="dot high"></span></td></tr>
  </table>

  <ul class="legend">
    <li><span class="dot avg"></span>avarage competence level</li>
    <li><span class="dot high"></span>highest competence level in the group</li>
  </ul>

  <div class="pattern-band" role="img" aria-label="Decorative diagonal stripe pattern in yellow and off-white"></div>
  <svg class="arc" width="848" height="150" viewBox="0 0 848 150" aria-hidden="true">
    <path d="M142 2 L691 2 Q560 145 420 145 Q270 145 142 2 Z" fill="var(--teal)"/>
  </svg>
  <div class="footer-band"></div>
</body>
</html>
```